Tamsel Loans - Mortgage Brokers Australia

redesign of tamselloans.com.au website. We are a mortgage brokering service and are clients are based in Australia. The demographics are 30-45 year holds looking to borrow money to purchase, invest and refinance property.

Please research other lending websites in Australia. My favourites are:

https://www.korvu.com.au/
https://www.brivanest.com.au/

I want CTA's on the first page. For Refinance/Purchase.

I DO NOT WANT ANYONE TO TRY AND CONTACT ME VIA EMAIL/What's app

My current website is: https/www.tamselloans.com.au/home and the password is "Rbqw8175?"

Target Market(s)

30-45 year hold professionals, first home buyers

Industry/Entity Type

Mortgage Brokerage

Number of Pages Required

4 page

Font styles to use
Sans Serif

Colors
e34197
6b449b
ffc214
0792cd
34a7d8

Requirements
Must have
• Must be fresh, clean and professional - with a beautiful hero section

```html
<!DOCTYPE html>
<html lang="en">
<head>
<meta charset="utf-8">
<title>Tamsel Loans – Mortgage Brokers Australia</title>
<link href="https://fonts.googleapis.com/css2?family=Poppins:wght@400;500;600&family=Nunito+Sans:wght@400;600;700;800&display=swap" rel="stylesheet">
<style>
:root{
  --pink:#e2579a;
  --purple:#6b4c9c;
  --purple-deep:#5b3f94;
  --band:#635096;
  --ink:#1f1d2b;
  --body:#55525f;
  --muted:#8d8a96;
  --hero:#f1eefa;
  --lav:#d9d0f0;
  --soft:#f4f4f6;
  --line:#dcdce2;
  --white:#ffffff;
}
*{box-sizing:border-box;margin:0;padding:0}
html,body{width:1200px;height:3565px;overflow:hidden}
body{position:relative;background:var(--white);font-family:"Nunito Sans",sans-serif;color:var(--ink)}
.abs{position:absolute}
a{color:inherit;text-decoration:none}

/* header + hero */
.hero{left:0;top:0;width:1200px;height:637px;background:linear-gradient(160deg,#f4f1fc 0%,#ece7f8 100%);overflow:hidden}
.hero-blob{left:560px;top:-40px;width:700px;height:680px;border-radius:48% 40% 42% 55%;background:#e6dff6}
.brand{font-family:"Nunito Sans",sans-serif;font-weight:700;color:var(--pink);font-size:27px;letter-spacing:-.3px}
.brand-mark{display:inline-block;width:12px;height:12px;background:var(--pink);margin-right:7px;vertical-align:2px}
.nav{top:43px;left:489px;display:flex;gap:0;font-family:"Poppins",sans-serif;font-size:13px;color:#2b2940}
.nav a{position:absolute;white-space:nowrap}
.hero-title{left:150px;top:236px;font-size:29px;line-height:44px;color:var(--ink);font-weight:400}
.hero-title strong{color:var(--purple);font-weight:700;font-size:35px}
.btn{display:flex;align-items:center;justify-content:center;gap:12px;height:41px;border-radius:21px;color:var(--white);font-size:15px;font-weight:600;box-shadow:0 8px 16px rgba(107,76,156,.25)}
.btn svg{width:24px;height:10px}
.btn-pink{background:var(--pink)}
.btn-purple{background:var(--purple)}
.hero-art{left:567px;top:180px;width:533px;height:387px;border-radius:40px 40px 120px 40px;background:linear-gradient(135deg,#c9bdee 0%,#b9a9e6 45%,#f0b8cf 100%)}
.dot{border-radius:50%;background:#e1dbf3}

/* partners */
.partners{top:690px;left:131px;width:935px;display:flex;justify-content:space-between;align-items:center}
.partner{font-family:"Nunito Sans",sans-serif;font-weight:700;font-size:21px;color:#3a3845}
.rule{left:123px;top:775px;width:954px;height:1px;background:var(--line)}

/* process */
.sec-title{font-family:"Poppins",sans-serif;font-weight:500;color:var(--purple-deep);text-align:center;width:1200px;left:0}
.sec-lead{width:1200px;left:0;text-align:center;font-size:13.5px;line-height:24px;color:var(--body)}
.feature-icon{width:76px;height:76px;border-radius:50%;border:2px dashed #c9c2dd;background:radial-gradient(circle,#7a5cb0 0 40%,#efeaf8 41%)}
.feature h3{font-size:17px;font-weight:600;color:var(--ink);margin-bottom:8px}
.feature p{font-size:14px;line-height:20px;color:var(--body)}
.photo-keys{left:599px;top:991px;width:450px;height:410px;background:linear-gradient(135deg,#6e5b4a 0%,#a89a88 40%,#d8d2c8 70%,#9a8f80 100%)}

/* services band */
.band{left:0;top:1507px;width:1200px;height:608px;background:var(--band)}
.band-title{top:1570px;font-family:"Poppins",sans-serif;font-size:31px;font-weight:500;color:var(--white)}
.band-lead{top:1622px;color:#e6e0f3;font-size:13.5px;line-height:22px}
.service{width:286px;text-align:center;color:var(--white)}
.service h3{font-family:"Poppins",sans-serif;font-size:17px;font-weight:500;margin:22px 0 14px}
.service p{font-size:13.5px;line-height:22px}
.service svg{width:72px;height:72px}
.service-card{left:458px;top:1705px;width:285px;height:341px;background:var(--white);border-radius:4px;box-shadow:0 10px 30px rgba(0,0,0,.18)}
.service-card .service{color:var(--ink)}
.service-card p{color:var(--muted)}

/* blog */
.post{width:278px;height:367px;background:var(--white);box-shadow:0 6px 20px rgba(30,20,60,.09)}
.post-img{width:278px;height:248px}
.post-meta{position:absolute;left:18px;top:270px;font-size:11.5px;color:var(--body);display:flex;align-items:center;gap:6px}
.post-title{position:absolute;left:18px;top:297px;width:245px;font-size:14px;line-height:21px;color:var(--ink)}
.circle-btn{width:32px;height:32px;border-radius:50%;display:flex;align-items:center;justify-content:center}
.circle-ghost{background:#ece8f5;border:1px solid #c9c0e0}
.circle-solid{background:var(--purple)}

/* about */
.about{left:0;top:2657px;width:1200px;height:523px;background:var(--soft);overflow:hidden}
.about-img{left:137px;top:2718px;width:395px;height:395px;border-radius:50%;background:radial-gradient(circle at 45% 55%,#b88e6a 0%,#8a6547 35%,#3d5672 70%,#22334a 100%)}
.eyebrow{left:621px;top:2763px;font-size:13px;font-weight:800;color:var(--ink);letter-spacing:.2px}
.about-title{left:621px;top:2796px;font-size:32px;line-height:40px;font-weight:700;color:var(--ink);letter-spacing:-.5px}
.about-text{left:621px;top:2898px;width:430px;font-size:15.5px;line-height:26px;color:var(--body)}

/* footer */
.foot-head{font-family:"Poppins",sans-serif;font-size:17px;font-weight:500;color:var(--ink)}
.foot-links{list-style:none;font-size:13px;color:var(--body)}
.foot-links li{height:25.6px;display:flex;align-items:center;gap:8px}
.foot-links svg{width:6px;height:10px}
.subscribe{left:693px;top:3293px;width:308px;height:36px;border:1px solid #c9c6d3;border-radius:18px;display:flex;overflow:hidden}
.subscribe span{flex:1;padding-left:22px;line-height:34px;font-size:13px;color:var(--muted)}
.subscribe b{width:104px;background:var(--purple);color:var(--white);font-weight:600;font-size:14px;text-align:center;line-height:34px}
.social{width:38px;height:38px;border-radius:50%;background:var(--purple)}
.foot-rule{left:0;top:3488px;width:1200px;height:1px;background:var(--line)}
.legal{top:3516px;font-size:12.5px;color:var(--body)}
</style>
</head>
<body>

<!-- Hero -->
<section class="hero abs">
  <div class="hero-blob abs"></div>
  <div class="dot abs" style="left:75px;top:410px;width:22px;height:22px"></div>
  <div class="dot abs" style="left:30px;top:475px;width:44px;height:44px"></div>
</section>

<a class="brand abs" style="left:150px;top:50px"><span class="brand-mark"></span>Tamsel Loans</a>

<nav class="nav abs" style="left:0;top:43px;width:1200px">
  <a style="left:489px">HOME</a>
  <a style="left:558px">SERVICES</a>
  <a style="left:655px">ABOUT US</a>
  <a style="left:752px">WHY USE BROKER</a>
  <a style="left:901px">BLOG</a>
  <a style="left:965px">CONTACT US</a>
</nav>

<h1 class="hero-title abs">We are passionate about<br>helping you <strong>Achieve<br>your financial goals!</strong></h1>

<a class="btn btn-pink abs" style="left:150px;top:413px;width:157px">Refinance
  <svg viewBox="0 0 24 10"><path d="M0 5h22M18 1l4 4-4 4" stroke="#fff" stroke-width="1.4" fill="none"/></svg></a>
<a class="btn btn-purple abs" style="left:320px;top:413px;width:158px">Purchase
  <svg viewBox="0 0 24 10"><path d="M0 5h22M18 1l4 4-4 4" stroke="#fff" stroke-width="1.4" fill="none"/></svg></a>

<div class="hero-art abs" role="img" aria-label="Illustration of a family of four standing beside a suburban home"></div>

<svg class="abs" style="left:590px;top:555px" width="18" height="32" viewBox="0 0 18 32" aria-label="Scroll down">
  <rect x="1" y="1" width="16" height="30" rx="8" fill="none" stroke="#8d84ad" stroke-width="1.5"/>
  <line x1="9" y1="7" x2="9" y2="12" stroke="#8d84ad" stroke-width="1.5"/>
</svg>

<!-- Partners -->
<div class="partners abs">
  <span class="partner">Harlow Bank</span>
  <span class="partner">Meridel Finance</span>
  <span class="partner">Quorra</span>
  <span class="partner">Tallis Bank</span>
  <span class="partner">Vessa</span>
  <span class="partner">Ondrel</span>
</div>
<div class="rule abs"></div>

<!-- Process -->
<h2 class="sec-title abs" style="top:837px;font-size:29px">The new way to get your mortage</h2>
<p class="sec-lead abs" style="top:889px">Tamsel Loans manage the entire process for you from start to finish and as every one of our clients is different,<br>we fully assess your individual situation and provide a solution to meet your particular needs.</p>

<div class="feature-icon abs" style="left:155px;top:1007px" role="img" aria-label="Icon of a house with charts and coins"></div>
<div class="feature abs" style="left:260px;top:1007px;width:300px">
  <h3>We work for you, not the lenders</h3>
  <p>Choosing the right home loan is like finding<br>the right match, but you need more.</p>
</div>
<div class="feature-icon abs" style="left:155px;top:1127px" role="img" aria-label="Icon of a building with a padlock and money"></div>
<div class="feature abs" style="left:260px;top:1128px;width:300px">
  <h3>We'll find you the perfect match</h3>
  <p>We're all about helping you reach your next<br>financial goal</p>
</div>
<div class="feature-icon abs" style="left:155px;top:1243px" role="img" aria-label="Icon of documents with a dollar coin"></div>
<div class="feature abs" style="left:260px;top:1243px;width:320px">
  <h3>We Are Fully Dedicated To Support You</h3>
  <p>We assess &amp; tailor your mortgage to suit your<br>financial situation</p>
</div>

<a class="btn btn-purple abs" style="left:263px;top:1351px;width:157px">Book Now
  <svg viewBox="0 0 24 10"><path d="M0 5h22M18 1l4 4-4 4" stroke="#fff" stroke-width="1.4" fill="none"/></svg></a>

<div class="photo-keys abs" role="img" aria-label="Photo of a hand holding house keys over a floor plan and calculator"></div>

<!-- Services -->
<section class="band abs"></section>
<h2 class="sec-title band-title abs">Nearly We Have Been Trying To Provide Those</h2>
<p class="sec-lead band-lead abs">Excepteur sint occaecat cupidatat non proident sunt in culpa qui officia deserunt<br>mollit lorem ipsum anim id est laborum perspiciatis unde.</p>

<div class="service abs" style="left:163px;top:1763px">
  <svg viewBox="0 0 72 72" fill="none" stroke="#fff" stroke-width="2"><path d="M8 38l18-14 18 14v24H8z"/><rect x="18" y="46" width="8" height="8"/><circle cx="50" cy="32" r="14"/><path d="M54 26h-6a3 3 0 000 6h4a3 3 0 010 6h-6M50 22v20"/><path d="M30 62h34"/></svg>
  <h3>Home Loans</h3>
  <p>There are many variations of<br>passages of lorem Ipsum but<br>majority have suffered.</p>
</div>
<div class="service-card abs">
  <div class="service" style="position:absolute;left:0;top:58px;width:285px">
    <svg viewBox="0 0 72 72" fill="none" stroke="#e2579a" stroke-width="2"><path d="M14 24a26 26 0 0146-6M58 48a26 26 0 01-46 6"/><path d="M60 10v9h-9M12 62v-9h9"/><path d="M24 38l12-10 12 10v12H24z"/><rect x="32" y="42" width="8" height="8"/></svg>
    <h3>Refinance</h3>
    <p>There are many variations of<br>passages of lorem Ipsum but<br>majority have suffered.</p>
  </div>
</div>
<div class="service abs" style="left:751px;top:1763px">
  <svg viewBox="0 0 72 72" fill="none" stroke="#fff" stroke-width="2"><circle cx="22" cy="50" r="14"/><path d="M26 44h-6a3 3 0 000 6h4a3 3 0 010 6h-6M22 40v20"/><path d="M34 38l28-28M50 10h12v12M40 54l22-22M54 32h8v8"/></svg>
  <h3>Investment Loans</h3>
  <p>There are many variations of<br>passages of lorem Ipsum but<br>majority have suffered.</p>
</div>

<!-- Blog -->
<div class="circle-btn circle-ghost abs" style="left:103px;top:2338px">
  <svg width="8" height="12" viewBox="0 0 8 12"><path d="M6 1L1 6l5 5" stroke="#6b4c9c" stroke-width="1.5" fill="none"/></svg></div>
<div class="circle-btn circle-ghost abs" style="left:1068px;top:2338px">
  <svg width="8" height="12" viewBox="0 0 8 12"><path d="M2 1l5 5-5 5" stroke="#6b4c9c" stroke-width="1.5" fill="none"/></svg></div>

<article class="post abs" style="left:150px;top:2203px">
  <div class="post-img" role="img" aria-label="Photo of a café worker handing takeaway cups to a customer" style="background:linear-gradient(135deg,#8a98b0,#c9b9a2 55%,#5e6d86)"></div>
  <div class="post-meta"><svg width="11" height="11" viewBox="0 0 12 12"><circle cx="6" cy="6" r="5" fill="none" stroke="#55525f"/><path d="M6 3v3l2 1" stroke="#55525f" fill="none"/></svg>13 Jun, 2018</div>
  <h3 class="post-title" style="font-weight:400">Flow of credit to small businesses remains strong</h3>
</article>
<article class="post abs" style="left:461px;top:2203px">
  <div class="post-img" role="img" aria-label="Photo of a smiling shop owner in an apron at a blue door" style="background:linear-gradient(135deg,#1f5c7a,#3f86a3 45%,#d7d2c7 70%,#2c6b86)"></div>
  <div class="post-meta"><svg width="11" height="11" viewBox="0 0 12 12"><circle cx="6" cy="6" r="5" fill="none" stroke="#55525f"/><path d="M6 3v3l2 1" stroke="#55525f" fill="none"/></svg>13 Jun, 2018</div>
  <h3 class="post-title" style="font-weight:400">WageBridge 2.0 is about to begin: here's what you need to know</h3>
</article>
<div class="circle-btn circle-solid abs" style="left:584px;top:2553px">
  <svg width="8" height="12" viewBox="0 0 8 12"><path d="M2 1l5 5-5 5" stroke="#fff" stroke-width="1.5" fill="none"/></svg></div>
<article class="post abs" style="left:771px;top:2203px">
  <div class="post-img" role="img" aria-label="Aerial photo of a coastal suburb beside the ocean" style="background:linear-gradient(135deg,#2a4a5c,#6f7a6a 45%,#a99c84 60%,#1e5269)"></div>
  <div class="post-meta"><svg width="11" height="11" viewBox="0 0 12 12"><circle cx="6" cy="6" r="5" fill="none" stroke="#55525f"/><path d="M6 3v3l2 1" stroke="#55525f" fill="none"/></svg>13 Jun, 2018</div>
  <h3 class="post-title" style="font-weight:400">Is now a good time to buy property? Two-thirds of investors say 'yes'</h3>
</article>

<!-- About -->
<section class="about abs"></section>
<div class="about-img abs" role="img" aria-label="Photo of hands holding a small wooden model house"></div>
<p class="eyebrow abs">ABOUT COMPANY</p>
<h2 class="about-title abs">We Focus on your needs,<br>not the banks</h2>
<p class="about-text abs">It is far too often that you hear of people ending up with the wrong type of loan, a bad deal, or sign up with promises that are never kept. Well, I am in the business of making sure that never happens to you.</p>
<a class="btn btn-purple abs" style="left:621px;top:3022px;width:158px">Learn More
  <svg viewBox="0 0 24 10"><path d="M0 5h22M18 1l4 4-4 4" stroke="#fff" stroke-width="1.4" fill="none"/></svg></a>

<!-- Footer -->
<a class="brand abs" style="left:205px;top:3284px"><span class="brand-mark"></span>Tamsel Loans</a>
<div class="abs" style="left:203px;top:3344px;display:flex;gap:10px;font-size:13px;line-height:20px;color:var(--body)">
  <svg width="14" height="18" viewBox="0 0 14 18"><path d="M7 1a6 6 0 016 6c0 4-6 10-6 10S1 11 1 7a6 6 0 016-6z" fill="none" stroke="#3a3845" stroke-width="1.5"/><circle cx="7" cy="7" r="2" fill="#3a3845"/></svg>
  <span>42 Calder Lane #5<br>Brisbane QLD 4000</span>
</div>
<div class="abs" style="left:202px;top:3399px;display:flex;gap:12px;align-items:center;font-size:16px;color:var(--purple)">
  <svg width="16" height="16" viewBox="0 0 16 16"><path d="M3 1l3 3-2 2c1 2 3 4 5 5l2-2 3 3-2 3C7 15 1 9 1 3z" fill="none" stroke="#3a3845" stroke-width="1.4"/></svg>
  (07) 5550 1234
</div>

<h4 class="foot-head abs" style="left:491px;top:3245px">COMPANY</h4>
<ul class="foot-links abs" style="left:493px;top:3282px">
  <li><svg viewBox="0 0 6 10"><path d="M1 1l4 4-4 4" stroke="#3a3845" fill="none"/></svg>Home</li>
  <li><svg viewBox="0 0 6 10"><path d="M1 1l4 4-4 4" stroke="#3a3845" fill="none"/></svg>Services</li>
  <li><svg viewBox="0 0 6 10"><path d="M1 1l4 4-4 4" stroke="#3a3845" fill="none"/></svg>About Us</li>
  <li><svg viewBox="0 0 6 10"><path d="M1 1l4 4-4 4" stroke="#3a3845" fill="none"/></svg>Why Use Broker</li>
  <li><svg viewBox="0 0 6 10"><path d="M1 1l4 4-4 4" stroke="#3a3845" fill="none"/></svg>Blog</li>
  <li><svg viewBox="0 0 6 10"><path d="M1 1l4 4-4 4" stroke="#3a3845" fill="none"/></svg>Contact Us</li>
</ul>

<h4 class="foot-head abs" style="left:702px;top:3245px">SUBSCRIBE</h4>
<div class="subscribe abs"><span>Email address</span><b>Subscribe</b></div>
<h4 class="foot-head abs" style="left:702px;top:3355px">FOLLOW US</h4>
<div class="social abs" style="left:701px;top:3394px" role="img" aria-label="Professional network profile"></div>
<div class="social abs" style="left:753px;top:3394px" role="img" aria-label="Photo sharing profile"></div>

<div class="foot-rule abs"></div>
<p class="legal abs" style="left:205px">© 2021 Tamsel Loans. All Rights Reserved.</p>
<p class="legal abs" style="left:855px">Privacy Policy &nbsp;|&nbsp; Terms of Use</p>

</body>
</html>
```